Web Site Redesign for Quellorainc.example

- Introduction

This is a web site redesign content. Please follow the following instructions. I am on tight schedule, so instead of 10 days, I would like to select the final design within 7 days. After the final design is selected, I would like the winner to produce the static HTML pages, but that is a separate job.

Delivery is JPG, complete Layered PSD files, and color numbers used in the design.

- Language of Content of the Web Site: English

- Company Name: Quellora, Inc.

- What is Quellora, Inc.'s product? Company develops and markets a sophisticated engineering simulation software.

- URL of existing web site: http://www.quellorainc.example

- Purpose of the web site: Marketing Engineering and Simulation Software

- Markets/Industries served

1. Medical: Radiotheraphy, Cancer Therapy, Medical Imaging
2. Energy: Nuclear Physics
3. National Security: Dept. of Coastal Surveying

- Three most important messages to communicate to our audience:

1. A solid and sophisticated engineering company (sophisticated).
2. A company with cutting-edge technology and leading products (cutting edge)
3. A company with state-of-art, live and professional marketing (state-of-the-art and live)

- What differentiates Quellora, Inc. from other competitors?

1. We are a commercial company vs. a home-grown entity with competitor products.
2. Our software is in-depth and targeted application vs. a general software with certain capabilities.

- Desired homepage screen size: 1280x800 or use your best recommendation.

- Number of templates: 2
1. Homepage
2. Secondary pages

- What content must be included in the Homepage (video, slideshow, etc.)?

1. Header block to display the logo, company name, and login or registration space (if user is logged in, show username)
2. One primary block to display a slide presentation (in HTML5, up to 4 or 5 slides with combined image and text)
3. One block to display a video and ability to play the video with a link "More" to go to the Video Training page.
4. One block to display announcements and special events
5. One block to display up to three News/Events. A Caption and Date.
6. One block to showcase links to three social networks: Chatterfold, Workloom, and Pipsqueal.
7. One block for Footer. Standard links and copyright notice

- Describe secondary pages: They will include text and images (JPG or PNG). A Training page will display a list of (up to 5) video clips.

- Site Menu Structure

1. Top Level. Up to 6 main menu as follows: Products, Support, Partners, Company, News/Events, and Purchase.

2. Second Level. Each top-level menu could have up to 4 sub-menu options. Some like Partners will not have any page. You don't have to display Third-level menus here.

3. Third Level. Some second-level menu items could have from up to 4 sub-menu options. Third-level menu options should appear in the template for secondary pages.

For example, under main menu "Products" we have three products one of which is "Borvek3QXRT." This product will have 4 options (4 pages). The template for the secondary pages should be flexible enough to allow for more than 4 but less than 6-7 options for each product.

(I will upload the Site Map document shortly)

- Style/theme of the Website:
1. Large enough font size. Audience is 30 and older.
2. Appealing to users of a highly-sophisticated desktop-based simulation software

- Desirable colors in the new design: Blue (because of logo), red, green, gray, black. White or Black background

- Adjectives that should best describe the new design: Welcoming, exciting, informative, and professional

- Websites you like (because?):

http://www.mendalux.example. Only because they also develop sophisticated software and they follow a similar licensing scheme, but PLEASE do not copy their UI.

Target Market(s)

- Age: 30 years and older
- Mostly male.
- Job Title: Researchers, Doctors, and Engineers
- Users of radiotheraphy, cancer therapy, medical imaging, nuclear energy, and homeland security radiation simulation software

Industry/Entity Type

Marketing

Requirements
Must have
• - What content must be included in the Homepage (video, slideshow, etc.)?

7. One block for Footer. Standard links and copyright notice.
Nice to have
• As you see I gave a thorough and detail design brief (I hope so). I leave it to you to incorporate "nice to haves" in your design.
Should not have
• - No Cartoonish Design or Animation
- Colors we do you NOT like: Purple, Pink, Yellow, Brown

```html
<!DOCTYPE html>
<html lang="en">
<head>
<meta charset="utf-8">
<title>Quellora Inc. — Radiation Transport Simulations</title>
<link href="https://fonts.googleapis.com/css2?family=Open+Sans:wght@300;400;600;700&display=swap" rel="stylesheet">
<style>
:root{
  --blue:#1f78c1;
  --blue-dark:#0f4f8a;
  --blue-deep:#0a3563;
  --sky:#4fa3e0;
  --green:#8cc63f;
  --red:#d7262b;
  --ink:#333;
  --muted:#666;
  --rule:#d8d8d8;
  --panel:#ececec;
  --footer:#2b2b2b;
  --base:#161616;
  --white:#fff;
}
*{box-sizing:border-box;margin:0;padding:0}
html,body{width:1200px;height:2372px;overflow:hidden}
body{font-family:"Open Sans",Arial,sans-serif;color:var(--ink);background:var(--white);font-size:15px;line-height:1.6}
a{color:inherit;text-decoration:none}
.wrap{width:1104px;margin:0 auto;position:relative}

/* header */
.site-header{height:108px;background:var(--white);position:relative}
.account{position:absolute;right:48px;top:0;display:flex;gap:4px}
.account a{background:var(--blue-deep);color:var(--white);font-size:13px;padding:4px 16px;border-radius:0 0 4px 4px}
.brand{position:absolute;left:48px;top:34px;display:flex;align-items:center;gap:12px}
.brand-mark{width:40px;height:40px;background:var(--blue);border-radius:50%}
.brand-name{font-size:28px;font-weight:700;color:var(--blue-dark);line-height:1}
.brand-tag{display:block;font-size:12px;color:var(--muted);margin-top:4px;letter-spacing:.5px}
.main-nav{position:absolute;right:48px;top:58px;display:flex;gap:34px;font-size:16px;color:var(--ink)}

/* hero */
.hero{height:492px;position:relative;background:linear-gradient(100deg,var(--blue-deep) 0%,var(--blue) 45%,var(--sky) 75%,#cfe6f7 100%)}
.hero-visual{position:absolute;right:0;top:0;width:660px;height:492px;background:radial-gradient(circle at 55% 45%,rgba(255,255,255,.55),rgba(120,190,240,.25) 35%,rgba(0,0,0,0) 65%)}
.hero-copy{position:absolute;left:48px;top:36px;width:420px;color:var(--white)}
.hero-title{font-size:30px;font-weight:400;background:rgba(5,40,80,.55);padding:6px 14px;margin-left:-14px;margin-bottom:18px}
.hero-copy p{font-size:16px;line-height:1.55}
.btn-green{display:inline-block;margin-top:26px;background:var(--green);color:var(--white);font-size:16px;font-weight:600;padding:8px 22px}

/* slide strip */
.slide-strip{height:135px;background:#202020;display:flex;justify-content:center;gap:12px;padding-top:16px}
.slide-thumb{width:152px;height:104px;border:2px solid #555;position:relative}
.slide-thumb.active{border-color:var(--white)}
.slide-thumb .shot{height:80px}
.slide-thumb span{display:block;background:#000;color:var(--white);font-size:11px;text-align:center;line-height:20px}
.t1 .shot{background:linear-gradient(135deg,#0d4d8c,#64b3ea)}
.t2 .shot{background:linear-gradient(135deg,#3b7a3b,#d8c23a 60%,#2a5da8)}
.t3 .shot{background:linear-gradient(135deg,#1a3f8a,#3aa0d8 50%,#c83b2e)}
.t4 .shot{background:linear-gradient(135deg,#1e2a7a,#4cb84a 50%,#e08a2a)}
.t5 .shot{background:linear-gradient(135deg,#222,#777)}
.oem{position:relative}

/* what we do */
.about{height:285px;padding-top:36px}
.section-title{font-size:30px;font-weight:400;text-align:center;color:#222;margin-bottom:14px}
.about p{font-size:15px;color:var(--muted);margin-bottom:14px}

/* video */
.video-block{height:400px;background:var(--panel)}
.video-block .wrap{display:flex;gap:60px;padding:32px 0 0 132px}
.player{width:480px}
.screen{height:270px;background:linear-gradient(160deg,#1b3a5c,#4b7fb0 60%,#8fb7d8);position:relative}
.play{position:absolute;left:50%;top:50%;width:72px;height:72px;margin:-36px 0 0 -36px}
.controls{height:30px;background:#111;display:flex;align-items:center;gap:10px;padding:0 10px}
.controls .bar{flex:1;height:4px;background:#555;position:relative}
.controls .bar i{position:absolute;left:0;top:0;height:4px;width:30%;background:var(--white)}
.btn-red{display:flex;width:280px;height:36px;margin:24px 0 0 20px;background:var(--red);color:var(--white);font-size:14px;font-weight:600;align-items:center;justify-content:center;gap:10px}
.video-copy{width:420px;padding-top:18px}
.video-copy h3{font-size:20px;font-weight:400;font-style:normal;margin-bottom:8px;color:#222}
.video-copy p{font-size:14px;color:var(--muted)}
.video-copy a{display:block;margin-top:14px;font-size:14px;color:var(--red);font-weight:600}

/* news + announcements */
.updates{height:420px;padding-top:18px}
.updates .wrap{display:flex;gap:60px}
.news{width:690px}
.col-title{font-size:22px;font-weight:400;color:var(--blue);margin-bottom:14px;border-bottom:1px solid var(--rule);padding-bottom:6px}
.feature{display:flex;gap:26px}
.feature-image{width:300px;height:150px;background:linear-gradient(135deg,#0d4d8c,#7fc0ee)}
.feature-text{width:340px;font-size:14px;color:var(--muted)}
.feature-text time{display:block;color:#222}
.feature-text h4{font-size:15px;font-weight:600;color:#222}
.feature-text a{color:var(--blue)}
.news-list{list-style:none;margin-top:20px;font-size:13px}
.news-list li{padding-left:14px;position:relative;margin-bottom:4px}
.news-list li::before{content:"";position:absolute;left:0;top:8px;width:6px;height:6px;border-radius:50%;background:var(--blue-dark)}
.news-list a{color:var(--blue)}
.announcements{width:354px}
.announce-list{list-style:none;font-size:13px}
.announce-list li{display:flex;gap:8px;align-items:center;border-bottom:1px solid var(--rule);padding:7px 0;color:var(--blue-dark)}

/* partners */
.partners{height:120px;background:var(--blue)}
.partners .wrap{display:flex;align-items:center;height:120px;gap:64px}
.partners h2{font-size:30px;font-weight:400;color:var(--white);width:140px}
.badge{width:110px;height:56px;border-radius:6px;background:rgba(255,255,255,.85)}
.badge.round{width:60px;border-radius:50%}

/* footer */
.site-footer{height:372px;background:var(--footer);color:#ccc}
.site-footer .wrap{display:flex;padding-top:32px;gap:40px}
.footer-contact{width:330px;font-size:13px;line-height:1.7}
.footer-brand{display:flex;align-items:center;gap:10px;margin-bottom:8px}
.footer-brand .brand-mark{width:32px;height:32px}
.footer-brand strong{font-size:24px;color:var(--white);font-weight:700}
.footer-brand small{display:block;font-size:11px;color:#aaa}
.footer-contact address{font-style:normal;margin-top:14px}
.map{margin-top:24px;width:210px;height:100px;background:linear-gradient(180deg,#3a3a3a,#2f2f2f)}
.social-col{width:300px}
.social-col h3,.tweet-col h3{font-size:18px;font-weight:400;color:var(--white);margin-bottom:10px;display:flex;align-items:center;gap:10px}
.ico{width:22px;height:22px;background:var(--blue);display:inline-block}
.widget{background:var(--white);color:var(--ink);padding:12px;font-size:12px}
.widget-head{display:flex;gap:10px;align-items:center;border-bottom:1px solid var(--rule);padding-bottom:8px}
.widget-head .sq{width:40px;height:40px;background:var(--blue)}
.fans{display:grid;grid-template-columns:repeat(5,1fr);gap:6px;margin-top:10px}
.fans i{height:44px;background:#c9d3df;display:block}
.tweet-col{width:340px;margin-left:auto}
.tweet{border-bottom:1px solid var(--rule);padding:8px 0;display:flex;gap:8px}
.tweet .sq{width:32px;height:32px;background:var(--blue);flex:none}
.tweet-box{margin-top:10px;border:1px solid var(--rule);padding:6px;color:#999}

.base-bar{height:40px;background:var(--base);color:#bbb;font-size:12px}
.base-bar .wrap{display:flex;justify-content:space-between;line-height:40px}
</style>
</head>
<body>

<header class="site-header">
  <div class="account"><a href="#">Login</a><a href="#">Register</a></div>
  <a class="brand" href="#">
    <span class="brand-mark"></span>
    <span><span class="brand-name">Quellora Inc.</span><span class="brand-tag">Radiation Transport Simulations</span></span>
  </a>
  <nav class="main-nav">
    <a href="#">Products</a><a href="#">Support</a><a href="#">Partners</a><a href="#">Company</a><a href="#">News/Events</a><a href="#">Contact</a>
  </nav>
</header>

<section class="hero">
  <div class="hero-visual" role="img" aria-label="Hand touching a glowing blue digital interface"></div>
  <div class="hero-copy">
    <h1 class="hero-title">Welcome to Quellora Inc.</h1>
    <p>At Quellora, Inc., we develop software solutions for accurately and rapidly predicting the macroscopic behavior of radiation. Since 2002, our products have been used worldwide for a diverse range of industries where radiation effects play an integral role in product performance, safety, and reliability.</p>
    <a class="btn-green" href="#">READ MORE</a>
  </div>
</section>

<div class="slide-strip">
  <div class="slide-thumb active t1"><div class="shot" role="img" aria-label="Welcome slide preview"></div><span>Welcome</span></div>
  <div class="slide-thumb t2"><div class="shot" role="img" aria-label="Simulation result preview"></div><span>KESTRAL</span></div>
  <div class="slide-thumb t3"><div class="shot" role="img" aria-label="Mesh model preview"></div><span>KESTRAL</span></div>
  <div class="slide-thumb t4"><div class="shot" role="img" aria-label="Dose map preview"></div><span>Borvek3QXRT</span></div>
  <div class="slide-thumb t5"><div class="shot" role="img" aria-label="OEM solutions preview"></div><span>OEM Solutions</span></div>
</div>

<section class="about">
  <div class="wrap">
    <h2 class="section-title">What We Do?</h2>
    <p>At Quellora, Inc., we develop software solutions for accurately and rapidly predicting the macroscopic behavior of radiation. Since 2002, our products have been used worldwide for a diverse range of industries where radiation effects play an integral role in product performance, safety, and reliability.</p>
    <p>Our team consists of internationally recognized experts in the research, development and application of radiation simulation software. All of our products are developed and maintained under an ISO 9001:2000 certified quality management system, and we have a proven track record in the development and commercialization of customer-specific OEM solutions.</p>
  </div>
</section>

<section class="video-block">
  <div class="wrap">
    <div class="player">
      <div class="screen" role="img" aria-label="Training video still frame">
        <svg class="play" viewBox="0 0 72 72"><circle cx="36" cy="36" r="34" fill="rgba(0,0,0,.55)" stroke="#fff" stroke-width="3"/><path d="M28 22 L52 36 L28 50Z" fill="#fff"/></svg>
      </div>
      <div class="controls">
        <svg width="12" height="14" viewBox="0 0 12 14"><path d="M0 0L12 7L0 14Z" fill="#fff"/></svg>
        <div class="bar"><i></i></div>
        <svg width="16" height="14" viewBox="0 0 16 14"><path d="M0 4H4L9 0V14L4 10H0Z" fill="#fff"/></svg>
      </div>
      <a class="btn-red" href="#">VIEW ALL VIDEOS
        <svg width="18" height="14" viewBox="0 0 18 14"><rect width="18" height="14" rx="3" fill="#fff"/><path d="M7 3.5L12 7L7 10.5Z" fill="#d7262b"/></svg>
      </a>
    </div>
    <div class="video-copy">
      <h3>Video Title:</h3>
      <p>This short clip walks through setting up a transport model, defining sources and materials, and running a first calculation. It is a good starting point for new users who want to see the full workflow from mesh import to viewing the final dose results in the viewer.</p>
      <a href="#">Click for more videos of this series</a>
    </div>
  </div>
</section>

<section class="updates">
  <div class="wrap">
    <div class="news">
      <h2 class="col-title">Latest News / Events</h2>
      <div class="feature">
        <div class="feature-image" role="img" aria-label="Screenshot of the new website"></div>
        <div class="feature-text">
          <time>September 30, 2013</time>
          <h4>OUR NEW SITE</h4>
          <p>Our redesigned site is now live, with easier access to product pages, training videos, support material and the latest release notes for every user.</p>
          <a href="#">» Read More</a>
        </div>
      </div>
      <ul class="news-list">
        <li>September 25, 2013 <a href="#">Version 8.2 release adds faster meshing and new reporting tools.</a></li>
        <li>September 20, 2013 <a href="#">Join our autumn user workshop on transport simulation methods.</a></li>
      </ul>
    </div>
    <aside class="announcements">
      <h2 class="col-title">Announcements</h2>
      <ul class="announce-list">
        <li><svg width="10" height="10"><path d="M2 1L8 5L2 9Z" fill="#1f78c1"/></svg>Quellora, Inc. Receives ISO 9001 Certification</li>
        <li><svg width="10" height="10"><path d="M2 1L8 5L2 9Z" fill="#1f78c1"/></svg>Quellora, Inc. Featured in the Harbor Ledger Weekly</li>
        <li><svg width="10" height="10"><path d="M2 1L8 5L2 9Z" fill="#1f78c1"/></svg>KESTRAL Version 8.0 Has Been Released</li>
        <li><svg width="10" height="10"><path d="M2 1L8 5L2 9Z" fill="#1f78c1"/></svg>Tellora RT Receives 510(k) Clearance</li>
        <li><svg width="10" height="10"><path d="M2 1L8 5L2 9Z" fill="#1f78c1"/></svg>Tellora BV Receives 510(k) Clearance</li>
        <li><svg width="10" height="10"><path d="M2 1L8 5L2 9Z" fill="#1f78c1"/></svg>KESTRAL Version 8.1 Has Been Released</li>
      </ul>
    </aside>
  </div>
</section>

<section class="partners">
  <div class="wrap">
    <h2>Partners</h2>
    <span class="badge"></span>
    <span class="badge round"></span>
    <span class="badge"></span>
    <span class="badge"></span>
  </div>
</section>

<footer class="site-footer">
  <div class="wrap">
    <div class="footer-contact">
      <div class="footer-brand"><span class="brand-mark"></span><span><strong>Quellora Inc.</strong><small>Radiation Transport Simulations</small></span></div>
      <address>Quellora, Inc., 4410 Marren Lane,<br>Suite B-210, Alder Point, WA 98000<br>Phone: 555.014.2290<br>Email: info@quellorainc.example</address>
      <div class="map" role="img" aria-label="Faint world map"></div>
    </div>
    <div class="social-col">
      <h3>Find us on <span class="ico"></span></h3>
      <div class="widget">
        <div class="widget-head"><span class="sq"></span><div><strong>Quellora Inc.</strong><br>Like · 212 people like this</div></div>
        <div class="fans" role="img" aria-label="Follower profile pictures">
          <i></i><i></i><i></i><i></i><i></i><i></i><i></i><i></i><i></i><i></i>
        </div>
        <p style="margin-top:8px;color:#999">Chatterfold social plugin</p>
      </div>
    </div>
    <div class="tweet-col">
      <h3>Tweet on <span class="ico"></span></h3>
      <div class="widget">
        <div class="tweet"><span class="sq"></span><p><strong>Quellora Inc.</strong> @quellorainc<br>New training videos are now online for all users. http://bit.ly/qk2</p></div>
        <div class="tweet"><span class="sq"></span><p><strong>Quellora Inc.</strong> @quellorainc<br>Version 8.2 is available for download now. http://bit.ly/qk3</p></div>
        <div class="tweet-box">Tweet to @quellorainc</div>
      </div>
    </div>
  </div>
</footer>

<div class="base-bar">
  <div class="wrap">
    <span>Copyright 2004 - 2013 by Quellora Inc. | All Rights Reserved</span>
    <span>Home | Products | Company | Terms | Privacy | Contact</span>
  </div>
</div>

</body>
</html>
```